Acupuncture business needs business card design

I need a business card for an acupuncture clinic called "Summit Wellpath"
It will need the following details:
My name: Marcus Thelwick
Acupuncturist
Member KPTG
BVF Treatment Provider
Ph numbers: 482 1358 027 514 3820
Email: marcus@swpath.example.nz
On the back it will need a table with 2 columns for appointments, one column for time and one for date.

Industry/Entity Type

Clinic

Contact Information for Business Card

Marcus Thelwick
Acupuncturist
Member KPTG
BVF Treatment Provider
Email: marcus@swpath.example.nz

Requirements
Must have
• Marcus Thelwick
• Acupuncturist
• Member KPTG
• BVF Treatment Provider
• Ph numbers: 482 1358 027 514 3820
• Email: marcus@swpath.example.nz
• On the back it will need a table with 2 columns for appointments, one column for time and one for date.

```html
<!DOCTYPE html>
<html lang="en">
<head>
<meta charset="utf-8">
<title>Summit Wellpath – Business Card</title>
<link href="https://fonts.googleapis.com/css2?family=Montserrat:wght@400;500;600&display=swap" rel="stylesheet">
<style>
  :root{
    --bg:#2a2a2c;
    --paper:#ffffff;
    --paper-shade:#e9ecee;
    --teal:#1a7d94;
    --teal-dark:#11687c;
    --sky:#2aa6d8;
    --sky-soft:#7fd0ee;
    --ink:#3f4448;
    --on-teal:#d9e8ec;
    --rule:#8fd0e6;
    --ghost:#eef1f3;
  }
  *{box-sizing:border-box;margin:0;padding:0}
  html,body{width:1200px;height:900px;overflow:hidden}
  body{background:var(--bg);font-family:"Montserrat",sans-serif;position:relative}
  .card{
    position:absolute;left:250px;width:700px;height:400px;border-radius:28px;
    overflow:hidden;background:linear-gradient(180deg,var(--paper) 0%,var(--paper-shade) 100%);
  }
  .card--back{top:40px}
  .card--front{top:460px}
  .card svg.shape{position:absolute;inset:0;width:700px;height:400px}
  .ghost-circle{position:absolute;left:300px;top:20px;width:280px;height:280px;border-radius:50%;background:var(--ghost)}

  /* back */
  .appointment{position:absolute;left:46px;top:30px;width:440px}
  .appointment__title{font-size:32px;font-weight:400;color:var(--sky);letter-spacing:.5px;margin-bottom:12px}
  .appointment__table{border-collapse:collapse;width:100%}
  .appointment__table td{height:36px;vertical-align:bottom;padding-bottom:4px;font-size:16px;color:var(--sky)}
  .appointment__table .label{width:54px}
  .appointment__table .line{border-bottom:1.5px solid var(--rule)}
  .appointment__table .gap{width:22px}

  .brand{position:absolute;display:flex;align-items:center;gap:14px}
  .brand__dot{width:46px;height:46px;border-radius:50%;background:var(--sky)}
  .brand__name{font-size:40px;font-weight:600;line-height:1;letter-spacing:-.5px}
  .brand__tag{font-size:13px;font-weight:500;letter-spacing:4.3px;margin-top:5px}
  .card--back .brand{left:46px;top:318px}
  .card--back .brand__name{color:var(--paper)}
  .card--back .brand__tag{color:var(--sky-soft)}
  .card--back .brand__dot{background:var(--paper)}

  /* front */
  .card--front .brand{left:40px;top:40px}
  .card--front .brand__name{color:var(--sky)}
  .card--front .brand__tag{color:var(--teal)}
  .person{position:absolute;left:44px;top:148px;color:var(--ink)}
  .person__name{font-size:19px;font-weight:600;color:var(--sky)}
  .person__role{font-size:20px;font-weight:500}
  .person__memb{font-size:13px;font-weight:500}
  .address{position:absolute;left:490px;top:232px;font-size:15px;line-height:1.4;color:var(--on-teal);font-style:normal}
  .contact{position:absolute;left:44px;top:275px;border-collapse:collapse}
  .contact td{font-size:18px;line-height:1.3;padding:0}
  .contact .k{color:var(--sky-soft);padding-right:14px}
  .contact .v{color:var(--paper)}
</style>
</head>
<body>

<section class="card card--back" aria-label="Card back: appointment table">
  <div class="ghost-circle"></div>
  <svg class="shape" viewBox="0 0 700 400" aria-hidden="true">
    <path d="M0,305 C320,305 580,240 700,80 L700,400 L0,400 Z" fill="var(--teal)"/>
    <path d="M300,282 C500,262 620,200 700,80 L700,96 C620,212 500,272 300,282 Z" fill="var(--sky)"/>
  </svg>
  <div class="appointment">
    <h2 class="appointment__title">Your Next Appointment</h2>
    <table class="appointment__table">
      <tr><td class="label">Date</td><td class="line"></td><td class="gap"></td><td class="label">Time</td><td class="line"></td></tr>
      <tr><td class="label">Date</td><td class="line"></td><td class="gap"></td><td class="label">Time</td><td class="line"></td></tr>
      <tr><td class="label">Date</td><td class="line"></td><td class="gap"></td><td class="label">Time</td><td class="line"></td></tr>
      <tr><td class="label">Date</td><td class="line"></td><td class="gap"></td><td class="label">Time</td><td class="line"></td></tr>
    </table>
  </div>
  <div class="brand">
    <span class="brand__dot"></span>
    <div>
      <div class="brand__name">Summit Wellpath</div>
      <div class="brand__tag">ACUPUNCTURE PHYSIOTHERAPY</div>
    </div>
  </div>
</section>

<section class="card card--front" aria-label="Card front: contact details">
  <svg class="shape" viewBox="0 0 700 400" aria-hidden="true">
    <path d="M0,255 C260,260 520,210 700,95 L700,400 L0,400 Z" fill="var(--teal)"/>
    <path d="M300,232 C480,215 610,160 700,95 L700,110 C610,170 480,222 300,232 Z" fill="var(--sky)"/>
  </svg>
  <div class="brand">
    <span class="brand__dot"></span>
    <div>
      <div class="brand__name">Summit Wellpath</div>
      <div class="brand__tag">ACUPUNCTURE PHYSIOTHERAPY</div>
    </div>
  </div>
  <div class="person">
    <div class="person__name">Marcus Thelwick</div>
    <div class="person__role">Acupuncturist</div>
    <div class="person__memb">Member KPTG, BVF Treatment Provider</div>
  </div>
  <address class="address">27c Harbourne Lane<br>(entry via Kestrel St)<br>Ashvale</address>
  <table class="contact">
    <tr><td class="k">Phone</td><td class="v">(09) 482 1358</td></tr>
    <tr><td class="k">Cell</td><td class="v">027 514 3820</td></tr>
    <tr><td class="k">Email</td><td class="v">marcus@swpath.example.nz</td></tr>
    <tr><td class="k">Web</td><td class="v">swpath.example.nz</td></tr>
  </table>
</section>

</body>
</html>
```